Kestrel Summit 2019 Enemies of the End-Times Church Flyer

We want a church conference flyer designed. We are looking for a professional, yet catchy design that uses our brand colors and logo creatively while communicating key information of the event effectively. <br/>The flyer must include all of the following:<br/>Title: Kestrel Summit 2019<br/>Topic: The Enemies of The End-Times Church <br/>Subtitles: <br/> -How the antichrist raises an army by social behavior engineering. <br/>-How the architects of modern social constructs escaped the church's radar. <br/>-The Holy Spirit's end-times agenda:<br/> The Knock-Out Punch!<br/>Speaker: Prophet Marcus Toliver <br/>Dates/time: December 27, 28 & 29 at 6pm<br/>Location: Halvorn Community Center <br/> 241 Pellham Street <br/> Portland, ME 04102<br/>Contact info: phone: 207-555-0148 <br/>email: contact@brookmeadow.example <br/> www.vutel.example<br/>*The flyer must also include a picture of the speaker and our Vutel logo <br/>Thanks, we look forward to seeing what you come up with!

Colors

Designer to choose colors to be used in the design.

Requirements
Must have
• The flyer must include all of the following:
• Title: Kestrel Summit 2019
• Topic: The Enemies of The End-Times Church
• Subtitles:
• -How the antichrist raises an army by social behavior engineering.
• -How the architects of modern social constructs escaped the church's radar.
• -The Holy Spirit's end-times agenda:
• The Knock-Out Punch!
• Speaker: Prophet Marcus Toliver
• Dates/time: December 27, 28 & 29 at 6pm
• Location: Halvorn Community Center
• 241 Pellham Street
• Portland, ME 04102
• Contact info: phone: 207-555-0148
• email: contact@brookmeadow.example
• www.vutel.example
• *The flyer must also include a picture of the speaker and our Vutel logo
Should not have
• Pictures of crosses or church buildings

```html
<!DOCTYPE html>
<html lang="en">
<head>
<meta charset="utf-8">
<title>Kestrel Summit 2019 – The Enemies of The End-Times Church</title>
<link rel="stylesheet" href="https://fonts.googleapis.com/css2?family=Montserrat:wght@400;500;600;700;800&family=Pinyon+Script&display=swap">
<style>
  :root {
    --orange: #f5862a;
    --navy: #163a5f;
    --ink: #3a3a3a;
    --white: #ffffff;
    --night: #16161b;
    --brick: #8f3a36;
    --sans: "Montserrat", Arial, sans-serif;
    --script: "Pinyon Script", cursive;
  }
  * { margin: 0; padding: 0; box-sizing: border-box; }
  html, body { width: 848px; height: 1200px; overflow: hidden; background: var(--night); }
  .flyer {
    position: relative; width: 848px; height: 1200px; overflow: hidden;
    font-family: var(--sans); color: var(--white);
  }
  .sky {
    position: absolute; inset: 0;
    background:
      radial-gradient(ellipse 340px 160px at 430px 300px, rgba(255,250,225,.95), rgba(255,240,200,0) 100%),
      linear-gradient(180deg, #f4f1ea 0%, #f1e6cf 18%, #f0cf92 30%, #e9a15a 40%, #b8623c 52%, #5e3b36 64%, #28252c 76%, #141418 100%);
  }
  .facets { position: absolute; inset: 0; }
  .title { position: absolute; left: 40px; top: 28px; font-weight: 600; line-height: 1; }
  .title .line { display: block; color: var(--orange); font-size: 84px; letter-spacing: -1px; }
  .title .line + .line { margin-top: -3px; }
  .title .year { display: block; color: var(--navy); font-size: 132px; font-weight: 700; margin-top: -4px; letter-spacing: -2px; }
  .topic-tab {
    position: absolute; left: 0; top: 316px; width: 190px; height: 38px;
    background: var(--orange); clip-path: polygon(0 0, 176px 0, 190px 50%, 176px 100%, 0 100%);
  }
  .topic-tab span {
    position: absolute; left: 48px; top: -8px; font-family: var(--script);
    color: #2a2520; font-size: 40px; font-weight: 700;
  }
  .topic {
    position: absolute; left: 26px; top: 352px; width: 797px; height: 57px;
    background: rgba(245,242,238,.82); color: var(--ink);
    font-size: 37.5px; font-weight: 600; line-height: 57px; padding-left: 20px; letter-spacing: .2px;
  }
  .points { position: absolute; left: 42px; top: 436px; list-style: none; }
  .points li { position: relative; padding-left: 41px; font-size: 24px; font-weight: 700; line-height: 28px; width: 660px; }
  .points li + li { margin-top: 28px; }
  .points li:last-child { font-weight: 600; }
  .points svg { position: absolute; left: 0; top: 4px; }
  .punch { display: block; color: var(--orange); font-size: 40px; font-weight: 800; line-height: 44px; margin-top: 6px; }
  .info { position: absolute; left: 44px; }
  .info svg { position: absolute; left: 0; top: 0; }
  .venue { top: 703px; }
  .venue .text { margin-left: 89px; font-size: 18.5px; line-height: 23px; font-weight: 500; padding-top: 9px; }
  .venue strong { font-weight: 700; font-size: 20.5px; }
  .when { top: 805px; }
  .when .text { margin-left: 89px; padding-top: 9px; }
  .when strong { display: block; font-size: 21px; font-weight: 700; line-height: 24px; }
  .when .time { display: block; font-size: 33px; font-weight: 400; line-height: 34px; }
  .contact-label { position: absolute; left: 46px; top: 906px; font-family: var(--script); color: var(--orange); font-size: 36px; }
  .contact { position: absolute; left: 48px; top: 962px; list-style: none; }
  .contact li { position: relative; padding-left: 42px; font-size: 24px; line-height: 32px; }
  .contact li:first-child { font-weight: 700; }
  .contact svg { position: absolute; left: 0; top: 6px; }
  .brand { position: absolute; left: 44px; top: 1118px; display: flex; align-items: center; gap: 10px;
    font-size: 40px; font-weight: 500; letter-spacing: 1px; color: var(--white); }
  .brand .dot { width: 16px; height: 16px; border-radius: 50%; background: var(--orange); }
  .rule { position: absolute; left: 238px; top: 1159px; width: 272px; height: 2px; background: var(--white); }
  .edge { position: absolute; left: 805px; top: 447px; width: 2px; height: 405px; background: var(--white); }
  .speaker-photo { position: absolute; left: 0; top: 0; }
  .speaker-label { position: absolute; left: 680px; top: 1052px; font-family: var(--script); color: var(--orange); font-size: 38px; }
  .speaker-band {
    position: absolute; left: 320px; top: 1092px; width: 528px; height: 38px;
    background: linear-gradient(90deg, rgba(160,110,50,0) 0%, rgba(160,110,50,.6) 40%, rgba(190,130,60,.85) 100%);
  }
  .speaker-name { position: absolute; right: 41px; top: 1095px; font-size: 27.5px; font-weight: 700; letter-spacing: .5px; line-height: 34px; }
</style>
</head>
<body>
<main class="flyer">
  <div class="sky" role="img" aria-label="Sunrise over a sea of clouds, fading into a dark night sky"></div>

  <svg class="facets" width="848" height="1200" viewBox="0 0 848 1200" aria-hidden="true">
    <polygon points="0,0 60,0 130,180 0,280" fill="rgba(255,255,255,.25)"/>
    <polygon points="0,100 24,150 0,200" fill="rgba(120,150,190,.35)"/>
    <polygon points="600,0 848,0 848,340 760,420" fill="rgba(200,215,235,.35)"/>
    <polygon points="595,245 848,140 848,620 700,480" fill="rgba(150,180,215,.3)"/>
    <polygon points="0,560 140,880 0,1200" fill="rgba(60,90,140,.28)"/>
    <polygon points="848,560 848,900 760,760" fill="rgba(40,60,100,.3)"/>
  </svg>

  <svg class="speaker-photo" width="848" height="1200" viewBox="0 0 848 1200" aria-hidden="true">
    <polygon points="570,716 848,716 848,758 590,758" fill="rgba(245,134,42,.55)"/>
    <polygon points="570,716 632,716 474,960 640,1200 570,1200 425,960" fill="var(--brick)" opacity=".85"/>
    <polygon points="590,758 848,758 848,1200 640,1200 520,960" fill="rgba(30,25,30,.6)"/>
  </svg>
  <svg class="speaker-photo" width="848" height="1200" viewBox="0 0 848 1200" role="img" aria-label="Portrait photo of speaker Prophet Marcus Toliver">
    <defs>
      <linearGradient id="portraitTone" x1="0" y1="0" x2="0" y2="1">
        <stop offset="0" stop-color="#6b4a3a"/>
        <stop offset=".45" stop-color="#7a2f30"/>
        <stop offset="1" stop-color="#2e2f36"/>
      </linearGradient>
    </defs>
    <path d="M600,652 Q680,630 740,680 Q770,760 740,840 Q830,870 848,900 L848,1200 L505,1200 Q510,960 600,860 Q580,760 600,652 Z" fill="url(#portraitTone)" opacity=".92"/>
  </svg>

  <h1 class="title">
    <span class="line">KESTREL</span>
    <span class="line">SUMMIT</span>
    <span class="year">2019</span>
  </h1>

  <div class="topic-tab"><span>Topic:</span></div>
  <h2 class="topic">The Enemies of The End-Times Church</h2>

  <ul class="points">
    <li><svg width="26" height="22" viewBox="0 0 26 22" aria-hidden="true"><path d="M2,2 L11,11 L2,20 M13,2 L22,11 L13,20" fill="none" stroke="#fff" stroke-width="3.5"/></svg>How the antichrist raises an army by social behavior engineering.</li>
    <li><svg width="26" height="22" viewBox="0 0 26 22" aria-hidden="true"><path d="M2,2 L11,11 L2,20 M13,2 L22,11 L13,20" fill="none" stroke="#fff" stroke-width="3.5"/></svg>How the architects of modern social constructs escaped the church's radar.</li>
    <li><svg width="26" height="22" viewBox="0 0 26 22" aria-hidden="true"><path d="M2,2 L11,11 L2,20 M13,2 L22,11 L13,20" fill="none" stroke="#fff" stroke-width="3.5"/></svg>The Holy Spirit's end-times agenda:<span class="punch">The Knock-Out Punch!</span></li>
  </ul>

  <div class="info venue">
    <svg width="74" height="76" viewBox="0 0 74 76" aria-hidden="true">
      <path d="M28,70 Q4,44 4,28 A26,26 0 0 1 56,26" fill="none" stroke="#fff" stroke-width="5" stroke-linecap="round"/>
      <circle cx="30" cy="28" r="9" fill="none" stroke="#fff" stroke-width="5"/>
      <path d="M34,52 L52,36 L70,52 L70,72 L34,72 Z" fill="none" stroke="#fff" stroke-width="5" stroke-linejoin="round"/>
      <rect x="48" y="58" width="8" height="8" fill="#fff"/>
    </svg>
    <p class="text"><strong>HALVORN COMMUNITY CENTER</strong><br>241 PELLHAM STREET<br>PORTLAND, ME 04102</p>
  </div>

  <div class="info when">
    <svg width="68" height="68" viewBox="0 0 68 68" aria-hidden="true">
      <path d="M40,64 L8,64 Q3,64 3,59 L3,12 Q3,7 8,7 L58,7 Q63,7 63,12 L63,36" fill="none" stroke="#fff" stroke-width="4.5"/>
      <path d="M16,2 V12 M28,2 V12 M40,2 V12 M52,2 V12" stroke="#fff" stroke-width="4.5"/>
      <g fill="#fff"><circle cx="16" cy="28" r="2.5"/><circle cx="26" cy="28" r="2.5"/><circle cx="36" cy="28" r="2.5"/><circle cx="46" cy="28" r="2.5"/><circle cx="16" cy="38" r="2.5"/><circle cx="26" cy="38" r="2.5"/><circle cx="16" cy="48" r="2.5"/><circle cx="26" cy="48" r="2.5"/></g>
      <circle cx="50" cy="52" r="13" fill="none" stroke="#fff" stroke-width="4.5"/>
      <path d="M50,45 V53 H56" fill="none" stroke="#fff" stroke-width="3.5"/>
    </svg>
    <p class="text"><strong>DECEMBER 27, 28 &amp; 29</strong><span class="time">6.00 PM</span></p>
  </div>

  <p class="contact-label">Contact info:</p>
  <ul class="contact">
    <li><svg width="28" height="22" viewBox="0 0 28 22" aria-hidden="true"><path d="M2,8 Q14,-2 26,8 L22,10 L19,6 L9,6 L6,10 Z" fill="#fff"/><path d="M7,10 L21,10 L25,21 L3,21 Z" fill="#fff"/></svg>207-555-0148</li>
    <li><svg width="26" height="20" viewBox="0 0 26 20" aria-hidden="true"><rect x="1" y="1" width="24" height="18" fill="#fff"/><path d="M1,1 L13,11 L25,1 M1,19 L10,9 M25,19 L16,9" fill="none" stroke="#16161b" stroke-width="1.8"/></svg>contact@brookmeadow.example</li>
    <li><svg width="26" height="26" viewBox="0 0 26 26" aria-hidden="true"><circle cx="13" cy="13" r="11" fill="#fff"/><path d="M2,13 H24 M13,2 V24 M4,7 H22 M4,19 H22" stroke="#16161b" stroke-width="1.5" fill="none"/><ellipse cx="13" cy="13" rx="5" ry="11" fill="none" stroke="#16161b" stroke-width="1.5"/></svg>www.vutel.example</li>
  </ul>

  <div class="brand"><span class="dot"></span>VUTEL</div>
  <div class="rule"></div>
  <div class="edge"></div>

  <p class="speaker-label">Speaker:</p>
  <div class="speaker-band"></div>
  <p class="speaker-name">PROPHET MARCUS TOLIVER</p>
</main>
</body>
</html>
```